Business Stationary & Card Design

Double sided business cards, letterhead, horizontal brochure, and envelope design using our logo. We want a modern minimal look. One side of the business card should be only our logo and maybe our slogan "Get It Done Right". The other side should include our coil spring and not the logo again. Watermark like (or not) positioned partially, horizontal, on angle, or a combination of. IF a background color or accent color is used we like blue (4885ed). The letterhead, brochure, and envelope design should be similar to the card. Except no solid background color.Maybe the spring at the bottom of the letterhead page watermark style and partial. Additional info on the business card should be present:
Employee Name
Position
Phone
Email
Address
The final design should communicate strength, simplicity, and newness.

Target Market(s)

35-55 Male & Female

Industry/Entity Type

Automotive

Contact Information for Business Card

One side of the double sided business card should be only our logo and maybe our slogan "Get It Done Right". The other side should include our coil spring and not the logo again. Watermark like (or not) positioned partially, horizontal, on angle, or a combination of. IF a background color or accent color is used we like blue (4885ed). Additional info on the business card should be present:
Employee Name
Position
Phone
Email
Address

Font styles to use
Other font styles liked:
• Use font that compliments the attached font. Maybe plain eurostyle?

Colors
0492cd
3276b5

Requirements
Must have
• Use the coil spring in a subtle unique way (s). Double sided business card
Should not have
• Clutter, colors that do not coordinate well with our logo. Fonts that do not compliment our font.

```html
<!DOCTYPE html>
<html lang="en">
<head>
<meta charset="utf-8">
<title>Coilright Motors — Stationery Set</title>
<link href="https://fonts.googleapis.com/css2?family=Lato:wght@400;700;900&family=Michroma&display=swap" rel="stylesheet">
<style>
  :root {
    --bg: #d6d7d9;
    --paper: #ffffff;
    --brand-blue: #0c91cb;
    --brand-yellow: #e2b71c;
    --ink: #1d1d1d;
    --muted: #666a70;
    --watermark: #f1f1f1;
  }
  * { box-sizing: border-box; margin: 0; padding: 0; }
  html, body { width: 1200px; height: 1200px; overflow: hidden; }
  body { background: var(--bg); font-family: "Lato", sans-serif; color: var(--ink); position: relative; }

  .piece { position: absolute; background: var(--paper); overflow: hidden; }
  .wordmark { font-family: "Lato", sans-serif; font-weight: 900; color: var(--brand-yellow); letter-spacing: 0.04em; white-space: nowrap; line-height: 1; }
  .watermark { position: absolute; background: linear-gradient(180deg, var(--watermark), #f7f7f7); border-radius: 40px 40px 0 0; }

  .contact-list { position: absolute; list-style: none; color: var(--ink); }
  .contact-list li { display: flex; align-items: center; gap: 4px; }
  .contact-list svg { fill: var(--brand-yellow); flex: none; }

  /* Brochure */
  .brochure { left: 199px; top: 65px; width: 747px; height: 263px; }
  .brochure .back-panel { position: absolute; left: 0; top: 0; width: 373px; height: 100%; }
  .brochure .cover-panel { position: absolute; left: 373px; top: 0; width: 374px; height: 100%; background: var(--brand-blue); display: flex; align-items: center; justify-content: center; padding-bottom: 40px; }
  .brochure .cover-panel .wordmark { font-size: 26px; }
  .brochure .contact-list { left: 44px; top: 194px; font-size: 3.4px; line-height: 1.5; }
  .brochure .address { position: absolute; left: 44px; top: 218px; font-size: 3.4px; }
  .brochure .watermark { left: 273px; top: 127px; width: 76px; height: 136px; }

  /* Envelope */
  .envelope-back { left: 61px; top: 566px; width: 464px; height: 232px; }
  .envelope-back .flap { position: absolute; left: 0; top: 0; width: 100%; height: 78px; background: var(--brand-blue); clip-path: polygon(0 0, 100% 0, 98.6% 82%, 97% 100%, 3% 100%, 1.4% 82%); }
  .envelope-front { left: 119px; top: 750px; width: 465px; height: 233px; }
  .envelope-front .wordmark { position: absolute; left: 39px; top: 39px; font-size: 22px; }
  .envelope-front .contact-list { left: 39px; top: 142px; font-size: 6.4px; line-height: 1.42; }
  .envelope-front .address { position: absolute; left: 39px; top: 189px; font-size: 6.4px; display: flex; gap: 4px; align-items: center; }
  .envelope-front .watermark { left: 359px; top: 86px; width: 82px; height: 147px; }

  /* Business card */
  .card-front { left: 557px; top: 426px; width: 201px; height: 114px; background: var(--brand-blue); display: flex; align-items: center; justify-content: center; }
  .card-front .wordmark { font-size: 14px; }
  .card-back { left: 557px; top: 554px; width: 201px; height: 116px; }
  .card-back .name { position: absolute; left: 23px; top: 22px; font-family: "Michroma", sans-serif; font-size: 6.2px; font-weight: 700; letter-spacing: 0.02em; }
  .card-back .role { position: absolute; left: 23px; top: 31px; font-size: 4.4px; color: var(--brand-yellow); }
  .card-back .contact-list { left: 23px; top: 50px; font-size: 3.6px; line-height: 1.55; }
  .card-back .address { position: absolute; left: 23px; top: 83px; font-size: 3.6px; line-height: 1.3; display: flex; gap: 3px; }
  .card-back .watermark { left: 151px; top: 36px; width: 44px; height: 80px; border-radius: 22px 22px 0 0; }

  /* Letterhead */
  .letterhead { left: 726px; top: 382px; width: 407px; height: 575px; }
  .letterhead .wordmark { position: absolute; left: 0; right: 0; top: 72px; text-align: center; font-size: 22px; }
  .letterhead .salutation { position: absolute; left: 46px; top: 150px; font-size: 6.6px; color: var(--muted); }
  .letterhead .letter-body { position: absolute; left: 46px; top: 182px; width: 314px; font-size: 6.3px; line-height: 1.3; color: var(--muted); text-align: justify; }
  .letterhead .letter-body p { margin-bottom: 9px; }
  .letterhead .letter-body .lead { font-weight: 700; color: #444; }
  .letterhead .signature { position: absolute; left: 46px; top: 398px; width: 62px; height: 16px; background: linear-gradient(90deg, #ececec, #f7f7f7); border-bottom: 0.8px solid var(--muted); }
  .letterhead .footer-block { position: absolute; left: 46px; border-left: 1.6px solid var(--brand-yellow); padding-left: 6px; }
  .letterhead .footer-block .contact-list { position: static; font-size: 4.8px; line-height: 1.5; }
  .letterhead .footer-block .contact-list svg { fill: var(--ink); }
  .letterhead .contacts-block { top: 482px; }
  .letterhead .address-block { top: 515px; }
  .letterhead .watermark { left: 280px; top: 390px; width: 102px; height: 185px; }
</style>
</head>
<body>

<svg width="0" height="0" style="position:absolute">
  <defs>
    <symbol id="icon-phone" viewBox="0 0 10 10"><path d="M2 1l2 2-1 1.2a6 6 0 0 0 2.8 2.8L7 6l2 2-1.2 1.2C4.5 9 1 5.5.8 2.2z"/></symbol>
    <symbol id="icon-mail" viewBox="0 0 10 10"><path d="M1 2.5h8v5H1z M1 2.5l4 3 4-3" /></symbol>
    <symbol id="icon-web" viewBox="0 0 10 10"><circle cx="5" cy="5" r="4"/></symbol>
    <symbol id="icon-pin" viewBox="0 0 10 10"><path d="M5 .5a3.3 3.3 0 0 0-3.3 3.3C1.7 6.3 5 9.5 5 9.5s3.3-3.2 3.3-5.7A3.3 3.3 0 0 0 5 .5z"/></symbol>
  </defs>
</svg>

<!-- Brochure -->
<section class="piece brochure">
  <div class="back-panel">
    <ul class="contact-list">
      <li>+012-555-0147</li>
      <li>info@coilright.com</li>
      <li>www.coilright.com</li>
    </ul>
    <p class="address">218 North Harbor Road Fairview, NY 13100</p>
    <div class="watermark" role="img" aria-label="Faint partial coil spring watermark"></div>
  </div>
  <div class="cover-panel">
    <span class="wordmark">COILRIGHT</span>
  </div>
</section>

<!-- Envelope back -->
<section class="piece envelope-back">
  <div class="flap"></div>
</section>

<!-- Envelope front -->
<section class="piece envelope-front">
  <span class="wordmark">COILRIGHT</span>
  <ul class="contact-list">
    <li><svg width="6" height="6"><use href="#icon-phone"/></svg>+012-555-0147</li>
    <li><svg width="6" height="6"><use href="#icon-mail"/></svg>info@coilright.com</li>
    <li><svg width="6" height="6"><use href="#icon-web"/></svg>www.coilright.com</li>
  </ul>
  <p class="address"><svg width="6" height="6" style="fill:var(--brand-yellow)"><use href="#icon-pin"/></svg>218 North Harbor Road Fairview, NY 13100</p>
  <div class="watermark" role="img" aria-label="Faint partial coil spring watermark"></div>
</section>

<!-- Business card front -->
<section class="piece card-front">
  <span class="wordmark">COILRIGHT</span>
</section>

<!-- Business card back -->
<section class="piece card-back">
  <h2 class="name">Daniel Moreno</h2>
  <p class="role">Agent</p>
  <ul class="contact-list">
    <li><svg width="4" height="4"><use href="#icon-phone"/></svg>+012-555-0147</li>
    <li><svg width="4" height="4"><use href="#icon-mail"/></svg>info@coilright.com</li>
    <li><svg width="4" height="4"><use href="#icon-web"/></svg>www.coilright.com</li>
  </ul>
  <p class="address"><svg width="4" height="4" style="fill:var(--brand-yellow)"><use href="#icon-pin"/></svg><span>218 North Harbor Road<br>Fairview, NY 13100</span></p>
  <div class="watermark" role="img" aria-label="Faint partial coil spring watermark"></div>
</section>

<!-- Letterhead -->
<section class="piece letterhead">
  <span class="wordmark">COILRIGHT</span>
  <p class="salutation">Dear, Mr________</p>
  <div class="letter-body">
    <p>Lorem Ipsum is simply dummy text of the printing and typesetting industry. Lorem Ipsum has been the industry's standard dummy text ever since the1500s,when an unknown printer took a galley of type and scrambled it to make a type specimen book. It has survived not only five centuries, but also the leap into electronic typesetting, remaining essentially unchanged. It was popularised in the 1960s with the release of Letraset sheets containing Lorem Ipsum passages,and more recently with desktop publishing software like Aldus PageMaker including versions of Lorem Ipsum.</p>
    <p class="lead">Lorem Ipsum is simply dummy text of the printing and typesetting industry. Lorem Ipsum has been the industry's standard dummy text ever since the1500s,when an unknown printer took a galley of type and scrambled it to make a type specimen book.</p>
    <p>Lorem Ipsum is simply dummy text of the printing and typesetting industry. Lorem Ipsum has been the industry's standard dummy text ever since the1500s,when an unknown printer took a galley of type and scrambled it to make a type specimen book. It has survived not only five centuries, but also the leap into electronic typesetting, remaining essentially unchanged.</p>
    <p>Lorem Ipsum is simply dummy text of the printing and typesetting industry. Lorem Ipsum has been the industry's standard dummy text ever since the1500s,when an unknown printer took a galley of type and scrambled it to make a type specimen book.</p>
    <p>Lorem Ipsum is simply dummy text of the printing and typesetting industry.</p>
  </div>
  <div class="signature" role="img" aria-label="Handwritten signature"></div>
  <div class="footer-block contacts-block">
    <ul class="contact-list">
      <li><svg width="4" height="4"><use href="#icon-phone"/></svg>+012-555-0147</li>
      <li><svg width="4" height="4"><use href="#icon-mail"/></svg>info@coilright.com</li>
      <li><svg width="4" height="4"><use href="#icon-web"/></svg>www.coilright.com</li>
    </ul>
  </div>
  <div class="footer-block address-block">
    <ul class="contact-list">
      <li><svg width="4" height="4"><use href="#icon-pin"/></svg>218 North Harbor Road Fairview, NY 13100</li>
    </ul>
  </div>
  <div class="watermark" role="img" aria-label="Faint partial coil spring watermark"></div>
</section>

</body>
</html>
```